3 Banner Designs

We are looking for someone to create 3 designs with the dimensions of 310mm wide x 432mm high with a 300dpi. This would just be a picture design only, NO FLASH req'd.

Each design would need to promote a different part:

- Like our Gatherly page; special offers (gatherly.example/CheapRunwayCarStayPerth)
- Leave a review on Rateloop (rateloop.example/biz/cheap-runway-car-stay-berry-hill)
- Our travel blog (blog.cheaprunwaycarstay.example)
Updates

The dimensions have changed to 310mm x 432mm.

Target Market(s)

Our target market is varied; the one thing that they have in common is that they travel.

Industry/Entity Type

Travel

Font styles to use
Sans Serif
Script

Colors

Designer to choose colors to be used in the design.

Requirements
Must have
• For the Gatherly banner, I would like it to be very simple with a solid blue background with the 'Gatherly Nod Icon' image with the text 'Special Offers, Travel Tips & Reviews' 'Like Our Gatherly page'.

For the Rateloop Ad, I would like it to be a solid red with the Rateloop! logo. Include the text 'Let us know what you thought of our service'.

I'd like something a little different about the third banner that directs users to our travel blog. Include the text 'For Tips and Tricks for your next holiday, check out our new Travel Blog'.

```html
<!DOCTYPE html>
<html lang="en">
<head>
<meta charset="utf-8">
<title>Cheap Runway Car Stay – banner samples</title>
<link rel="stylesheet" href="https://fonts.googleapis.com/css2?family=Roboto+Condensed:wght@700&display=swap">
<style>
  :root {
    --board: #e9e9e9;
    --board-light: #f7f7f7;
    --footer: #000000;
    --white: #ffffff;
    --brand-red: #e8221d;
    --blue-dark: #1646b4;
    --blue-mid: #2f8cf0;
    --red-dark: #8e0c15;
    --red-mid: #d81e2c;
    --orange-dark: #e8380f;
    --orange-mid: #ff7a1c;
    --badge-blue: #3b6fd8;
    --badge-red: #d6101c;
  }
  * { margin: 0; padding: 0; box-sizing: border-box; }
  html, body { width: 935px; height: 1200px; overflow: hidden; }
  body {
    position: relative;
    background: radial-gradient(ellipse at 50% 40%, var(--board-light), var(--board) 75%);
    font-family: "Roboto Condensed", "Arial Narrow", sans-serif;
    color: var(--white);
  }
  .banner {
    position: absolute;
    width: 266px;
    height: 750px;
    overflow: hidden;
    box-shadow: -8px 10px 22px rgba(0,0,0,0.35);
  }
  .banner--offers  { left: 109px; top: 66px;  background: linear-gradient(180deg, var(--blue-dark), var(--blue-mid) 55%, var(--blue-dark)); }
  .banner--review  { left: 345px; top: 145px; background: linear-gradient(180deg, var(--red-mid), var(--red-dark) 30%, var(--red-mid) 60%, var(--red-dark)); }
  .banner--blog    { left: 580px; top: 227px; background: linear-gradient(180deg, var(--orange-dark), var(--orange-mid) 55%, var(--orange-dark)); }
  .banner__art { position: absolute; inset: 0; }
  .brand {
    position: absolute;
    display: flex;
    align-items: center;
    gap: 8px;
  }
  .banner .brand { left: 28px; top: 22px; }
  .brand__ring {
    width: 62px; height: 62px;
    border-radius: 50%;
    border: 7px solid var(--white);
    flex: none;
  }
  .brand__name {
    font-size: 15px;
    line-height: 15px;
    font-weight: 700;
    color: var(--white);
    letter-spacing: 0.3px;
  }
  .message {
    position: absolute;
    left: 28px;
    width: 200px;
    font-size: 13px;
    line-height: 17px;
    font-weight: 700;
  }
  .banner--offers .message { top: 102px; }
  .banner--review .message { top: 102px; }
  .banner--blog .message {
    left: 20px; width: 226px;
    top: 612px;
    text-align: center;
    font-size: 15px;
    line-height: 20px;
  }
  .headline {
    position: absolute;
    left: 10px;
    font-size: 60px;
    line-height: 50px;
    font-weight: 700;
    white-space: nowrap;
    text-shadow: 0 2px 4px rgba(0,0,0,0.35);
  }
  .banner--offers .headline { top: 488px; }
  .banner--review .headline { top: 492px; }
  .badge {
    position: absolute;
    width: 56px; height: 56px;
    border-radius: 8px;
  }
  .banner--offers .badge { left: 100px; top: 616px; background: var(--badge-blue); }
  .banner--review .badge { left: 107px; top: 627px; background: var(--badge-red); box-shadow: 0 2px 5px rgba(0,0,0,0.35); }
  .link {
    position: absolute;
    left: 0; right: 0;
    text-align: center;
    font-size: 13px;
    line-height: 19px;
    font-weight: 700;
    white-space: nowrap;
  }
  .banner--offers .link { top: 682px; }
  .banner--review .link { top: 702px; left: 10px; text-align: left; }
  .banner--review .link span { display: block; }
  .banner--review .link span:first-child { padding-left: 48px; }
  .banner--blog .link { top: 686px; }
  .link__dot {
    display: inline-block;
    width: 14px; height: 14px;
    border-radius: 2px;
    background: var(--white);
    vertical-align: -2px;
    margin-right: 5px;
  }
  .footer {
    position: absolute;
    left: 0; top: 1045px;
    width: 935px; height: 155px;
    background: var(--footer);
  }
  .footer .brand { left: 62px; top: 30px; }
  .footer .brand__ring { width: 88px; height: 88px; border: 9px solid var(--brand-red); }
  .footer .brand__name { color: var(--brand-red); font-size: 18px; line-height: 18px; margin-top: 38px; }
  .footer__title {
    position: absolute;
    left: 543px; top: 46px;
    font-size: 52px;
    line-height: 60px;
    font-weight: 700;
    color: var(--white);
  }
</style>
</head>
<body>

  <section class="banner banner--offers">
    <svg class="banner__art" width="266" height="750" viewBox="0 0 266 750">
      <defs>
        <linearGradient id="offers-photo" x1="0" y1="0" x2="0" y2="1">
          <stop offset="0" stop-color="#9cc7ef"/>
          <stop offset="0.5" stop-color="#d9e6f1"/>
          <stop offset="0.62" stop-color="#8e9498"/>
          <stop offset="1" stop-color="#5b6570"/>
        </linearGradient>
      </defs>
      <path role="img" aria-label="Photo of a jet climbing over an airport car park and multi-storey parking building"
            fill="url(#offers-photo)"
            d="M0,240 Q120,160 266,172 L266,520 Q200,610 90,625 Q30,630 0,610 Z"/>
      <path d="M0,240 Q120,160 266,172" fill="none" stroke="#fff" stroke-width="7"/>
      <path d="M0,610 Q30,630 90,625 Q200,610 266,520" fill="none" stroke="#fff" stroke-width="7"/>
    </svg>
    <div class="brand"><span class="brand__ring"></span><span class="brand__name">CHEAP RUNWAY<br>CAR STAY</span></div>
    <p class="message">Special Offers, Travel Tips &amp; Reviews<br>Like Our Gatherly page</p>
    <h2 class="headline">Special<br>Offers</h2>
    <span class="badge"></span>
    <p class="link"><span class="link__dot"></span>gatherly.example/<br>CheapRunwayCarStayPerth</p>
  </section>

  <section class="banner banner--review">
    <svg class="banner__art" width="266" height="750" viewBox="0 0 266 750">
      <defs>
        <linearGradient id="review-photo" x1="0" y1="0" x2="0" y2="1">
          <stop offset="0" stop-color="#8fb2d8"/>
          <stop offset="0.4" stop-color="#5d7fa6"/>
          <stop offset="0.6" stop-color="#5a6372"/>
          <stop offset="1" stop-color="#2d333c"/>
        </linearGradient>
      </defs>
      <path role="img" aria-label="Photo of a floodlit open-air car park at dusk full of parked cars"
            fill="url(#review-photo)"
            d="M0,235 Q110,165 266,168 L266,560 Q180,610 80,600 Q30,595 0,585 Z"/>
      <path d="M0,235 Q110,165 266,168" fill="none" stroke="#fff" stroke-width="7"/>
      <path d="M0,585 Q30,595 80,600 Q180,610 266,560" fill="none" stroke="#fff" stroke-width="7"/>
    </svg>
    <div class="brand"><span class="brand__ring"></span><span class="brand__name">CHEAP RUNWAY<br>CAR STAY</span></div>
    <p class="message">Let us know what you thought<br>of our service</p>
    <h2 class="headline">Leave a<br>Review</h2>
    <span class="badge"></span>
    <p class="link"><span>rateloop.example/</span><span>biz/cheap-runway-car-stay-berry-hill</span></p>
  </section>

  <section class="banner banner--blog">
    <svg class="banner__art" width="266" height="750" viewBox="0 0 266 750">
      <defs>
        <linearGradient id="blog-photo" x1="0" y1="0" x2="0" y2="1">
          <stop offset="0" stop-color="#7fc0e6"/>
          <stop offset="0.5" stop-color="#cfe6f3"/>
          <stop offset="0.75" stop-color="#e6eef4"/>
          <stop offset="1" stop-color="#9aa6b2"/>
        </linearGradient>
      </defs>
      <path role="img" aria-label="Photo of a jet taking off above parked silver cars"
            fill="url(#blog-photo)"
            d="M0,230 Q120,170 266,178 L266,525 Q190,590 90,600 Q35,604 0,590 Z"/>
      <path d="M0,230 Q120,170 266,178" fill="none" stroke="#fff" stroke-width="7"/>
      <path d="M0,590 Q35,604 90,600 Q190,590 266,525" fill="none" stroke="#fff" stroke-width="7"/>
    </svg>
    <div class="brand"><span class="brand__ring"></span><span class="brand__name">CHEAP RUNWAY<br>CAR STAY</span></div>
    <p class="message">For Tips and Tricks for your next holiday, check out our new Travel Blog</p>
    <p class="link">blog.cheaprunwaycarstay.example</p>
  </section>

  <footer class="footer">
    <div class="brand"><span class="brand__ring"></span><span class="brand__name">CHEAP RUNWAY CAR STAY</span></div>
    <h1 class="footer__title">banner samples</h1>
  </footer>

</body>
</html>
```